Electrical contractor needs a flyer and business card

'Voltique - The Electrical Contractor' needs an a5 flyer designed which will showcase the work we undertake. We already have a logo - see attached
We operate in Devon and Cornwall in the UK in these 3 market sectors: Domestic, Commercial, Industrial.
The work we undertake is as follows:
House re-wires
New builds
RCD and consumer unit upgrades
Renovations
TV aerials & extra points
Data / phone / networking
Security and garden lighting
Extra external / internal sockets
Garage upgrades
LED and low energy lighting installs
We offer a free consumer unit and earthing check!
24 hour service.
prompt quality service with over 15 years experience
All our work is fully certified and guaranteed for a year
contact details:
Marcus Pelling
Owner
marcus@voltique-wiring.co.uk
www.voltique-wiring.co.uk
m: 07938661207
t: 01392 586 031
Servicing Devon & Cornwall
We also need a business card designed
many thanks
Raf
Target Market(s)
Domestic, Commercial, Industrial.
Industry/Entity Type
Contractor
Font styles to use
Other font styles liked:
- eurostile extended
Look and feel

```html
<!DOCTYPE html>
<html lang="en">
<head>
<meta charset="utf-8">
<title>Voltique - Flyer and Business Card</title>
<link href="https://fonts.googleapis.com/css2?family=Roboto:wght@400;500;700;900&family=Open+Sans:wght@400;600;700&display=swap" rel="stylesheet">
<style>
  :root {
    --teal: #26a19a;
    --teal-deep: #1b8882;
    --teal-ring: #7fc9c4;
    --blue: #1b88b3;
    --blue-badge: #2f6fa8;
    --orange: #e8572a;
    --yellow: #f4e23a;
    --ink: #2b2b2b;
    --grey: #5d5f61;
    --band: #3a3a3a;
    --paper: #ffffff;
    --photo-light: #e4e7ea;
    --photo-mid: #b9c1c8;
  }
  * { margin: 0; padding: 0; box-sizing: border-box; }
  html, body { width: 1200px; height: 1000px; overflow: hidden; background: var(--paper); }
  body { position: relative; font-family: "Roboto", Arial, sans-serif; }

  /* Flyer */
  .flyer { position: absolute; left: 24px; top: 22px; width: 674px; height: 956px; overflow: hidden; background: linear-gradient(180deg, #f4f5f6 0%, #e9ebed 100%); }
  .flyer-photo { position: absolute; left: 320px; top: 0; width: 354px; height: 470px; background: linear-gradient(160deg, var(--photo-light) 0%, var(--photo-mid) 55%, #8e9aa4 100%); }
  .flyer-waves { position: absolute; left: 0; top: 380px; width: 674px; height: 576px; }
  .badge { position: absolute; left: 34px; top: 30px; width: 300px; height: 94px; border-radius: 26px; background: var(--blue-badge); display: flex; align-items: center; justify-content: center; }
  .badge-name { color: var(--paper); font-weight: 900; font-size: 46px; letter-spacing: 1px; }
  .corner-brand { position: absolute; right: 22px; top: 24px; display: flex; align-items: center; gap: 8px; }
  .corner-brand .dot { width: 20px; height: 20px; border-radius: 50%; background: var(--teal); }
  .corner-brand .name { font-weight: 700; font-size: 20px; color: var(--grey); letter-spacing: 3px; }
  .serving { position: absolute; left: 78px; top: 144px; }
  .serving-lead { font-weight: 700; font-size: 24px; color: var(--ink); }
  .serving-area { font-weight: 900; font-size: 34px; line-height: 36px; color: var(--orange); margin-top: 2px; }
  .sectors { position: absolute; left: 80px; top: 260px; list-style: none; }
  .sectors li { font-size: 23px; color: var(--grey); height: 35px; display: flex; align-items: center; gap: 4px; }
  .bolt { width: 14px; height: 18px; flex: none; }
  .photo-circle { position: absolute; border-radius: 50%; border: 8px solid var(--teal-ring); background: radial-gradient(circle at 45% 40%, #d9dde1 0%, #9aa5ae 70%, #6d7882 100%); }
  .c1 { left: 52px; top: 395px; width: 182px; height: 182px; }
  .c2 { left: 246px; top: 418px; width: 176px; height: 176px; background: radial-gradient(circle at 45% 45%, #f3f0ea 0%, #e2b48e 60%, #c98a4f 100%); }
  .c3 { left: 456px; top: 395px; width: 182px; height: 182px; }
  .services { position: absolute; left: 50px; top: 604px; list-style: none; }
  .services li { font-size: 15.5px; color: var(--paper); line-height: 19.4px; display: flex; gap: 6px; }
  .services li .bolt { width: 8px; height: 12px; margin-top: 4px; }
  .services .indent { padding-left: 8px; }
  .divider { position: absolute; left: 333px; top: 603px; width: 2px; height: 222px; background: rgba(255,255,255,0.85); }
  .offer { position: absolute; left: 364px; top: 604px; width: 300px; color: var(--paper); }
  .offer-free { font-weight: 700; font-size: 15.5px; line-height: 19px; }
  .offer-hours { font-size: 25px; color: var(--yellow); margin-top: 14px; letter-spacing: 0.3px; }
  .offer-text { font-size: 16px; line-height: 19px; margin-top: 12px; }
  .owner-name { font-weight: 700; font-size: 16.5px; color: var(--yellow); margin-top: 14px; }
  .owner-role { font-size: 14px; margin-left: 79px; }
  .flyer-area { position: absolute; left: 0; width: 674px; top: 844px; text-align: center; color: var(--paper); font-size: 13.5px; }
  .contact-band { position: absolute; left: 0; top: 866px; width: 674px; height: 33px; background: var(--band); color: var(--paper); font-weight: 700; font-size: 16px; display: flex; align-items: center; justify-content: center; letter-spacing: 0.3px; }
  .flyer-phone { position: absolute; left: 0; top: 898px; width: 674px; height: 58px; text-align: center; font-weight: 900; font-size: 40px; line-height: 58px; color: #333; letter-spacing: 2px; }

  /* Business card front */
  .card-front { position: absolute; left: 718px; top: 204px; width: 458px; height: 266px; background: var(--blue); padding: 22px; }
  .card-front-inner { position: relative; width: 100%; height: 100%; background: var(--paper); }
  .card-brand { display: flex; align-items: center; gap: 6px; font-family: "Open Sans", Arial, sans-serif; }
  .card-brand .dot { width: 16px; height: 16px; border-radius: 50%; background: var(--teal); }
  .card-brand .name { font-weight: 600; font-size: 20px; letter-spacing: 3px; color: var(--grey); }
  .card-front .card-brand { position: absolute; left: 123px; top: 100px; }
  .card-area { font-family: "Open Sans", Arial, sans-serif; font-size: 11px; color: #222; }
  .card-front .card-area { position: absolute; left: 0; width: 100%; bottom: 12px; text-align: center; }

  /* Business card back */
  .card-back { position: absolute; left: 718px; top: 494px; width: 458px; height: 272px; background: var(--paper); border: 1px solid #c9d5dc; font-family: "Open Sans", Arial, sans-serif; }
  .back-band-left { position: absolute; left: 0; top: 69px; width: 30px; height: 15px; background: var(--blue); }
  .back-band-right { position: absolute; left: 167px; top: 69px; width: 290px; height: 15px; background: var(--blue); }
  .back-name { position: absolute; left: 36px; top: 62px; font-family: "Roboto", Arial, sans-serif; font-weight: 900; font-size: 14.5px; color: #111; }
  .back-role { position: absolute; left: 36px; width: 122px; top: 80px; text-align: right; font-size: 10px; color: #111; }
  .card-back .card-brand { position: absolute; left: 32px; top: 160px; }
  .card-back .card-brand .name { font-size: 17px; letter-spacing: 2.5px; }
  .back-divider { position: absolute; left: 233px; top: 140px; width: 2px; height: 62px; background: #888; }
  .back-contacts { position: absolute; right: 14px; top: 138px; list-style: none; text-align: right; font-size: 10.5px; color: #111; }
  .back-contacts li { height: 17px; display: flex; align-items: center; justify-content: flex-end; gap: 4px; }
  .back-contacts svg { width: 11px; height: 11px; }
  .card-back .card-area { position: absolute; left: 0; width: 100%; top: 208px; text-align: center; }
  .back-footer { position: absolute; left: 0; bottom: 0; width: 100%; height: 36px; background: var(--blue); }
</style>
</head>
<body>

<section class="flyer" aria-label="Voltique flyer">
  <div class="flyer-photo" role="img" aria-label="Photo of an electrician working on a distribution board"></div>

  <svg class="flyer-waves" viewBox="0 0 674 576" preserveAspectRatio="none" aria-hidden="true">
    <defs>
      <linearGradient id="tealFill" x1="0" y1="0" x2="0" y2="1">
        <stop offset="0" stop-color="#2aa8a0"/>
        <stop offset="1" stop-color="#1f8f89"/>
      </linearGradient>
    </defs>
    <path d="M0 30 C120 -10 250 20 340 80 C440 140 560 110 674 60 L674 576 L0 576 Z" fill="#4a4d50"/>
    <path d="M0 90 C120 40 240 70 340 120 C450 170 570 150 674 110 L674 576 L0 576 Z" fill="url(#tealFill)"/>
  </svg>

  <div class="badge"><span class="badge-name">VOLTIQUE</span></div>

  <div class="corner-brand"><span class="dot"></span><span class="name">VOLTIQUE</span></div>

  <div class="serving">
    <p class="serving-lead">We Serving</p>
    <p class="serving-area">DEVON AND<br>CORNWALL</p>
  </div>

  <ul class="sectors">
    <li><svg class="bolt" viewBox="0 0 14 18"><path d="M3 0 L10 6 L6 7 L12 12 L8 13 L14 18 L1 11 L5 10 L0 5 L4 4 Z" fill="#5d5f61"/></svg>Domestic</li>
    <li><svg class="bolt" viewBox="0 0 14 18"><path d="M3 0 L10 6 L6 7 L12 12 L8 13 L14 18 L1 11 L5 10 L0 5 L4 4 Z" fill="#5d5f61"/></svg>Commercial</li>
    <li><svg class="bolt" viewBox="0 0 14 18"><path d="M3 0 L10 6 L6 7 L12 12 L8 13 L14 18 L1 11 L5 10 L0 5 L4 4 Z" fill="#5d5f61"/></svg>Industrial.</li>
  </ul>

  <div class="photo-circle c1" role="img" aria-label="Photo of gloved hands testing a board with a multimeter"></div>
  <div class="photo-circle c2" role="img" aria-label="Photo of a multimeter, tools, hard hat and model house"></div>
  <div class="photo-circle c3" role="img" aria-label="Photo of electricians wiring an industrial panel"></div>

  <ul class="services">
    <li><svg class="bolt" viewBox="0 0 8 12"><path d="M5 0 L1 6 L4 6 L2 12 L7 5 L4 5 Z" fill="#fff"/></svg>House re-wires</li>
    <li><svg class="bolt" viewBox="0 0 8 12"><path d="M5 0 L1 6 L4 6 L2 12 L7 5 L4 5 Z" fill="#fff"/></svg>New builds</li>
    <li><svg class="bolt" viewBox="0 0 8 12"><path d="M5 0 L1 6 L4 6 L2 12 L7 5 L4 5 Z" fill="#fff"/></svg>RCD and consumer unit</li>
    <li class="indent">upgrades</li>
    <li><svg class="bolt" viewBox="0 0 8 12"><path d="M5 0 L1 6 L4 6 L2 12 L7 5 L4 5 Z" fill="#fff"/></svg>Renovations</li>
    <li><svg class="bolt" viewBox="0 0 8 12"><path d="M5 0 L1 6 L4 6 L2 12 L7 5 L4 5 Z" fill="#fff"/></svg>TV aerials &amp; extra points</li>
    <li><svg class="bolt" viewBox="0 0 8 12"><path d="M5 0 L1 6 L4 6 L2 12 L7 5 L4 5 Z" fill="#fff"/></svg>Data / phone / networking</li>
    <li><svg class="bolt" viewBox="0 0 8 12"><path d="M5 0 L1 6 L4 6 L2 12 L7 5 L4 5 Z" fill="#fff"/></svg>Security and garden lighting</li>
    <li><svg class="bolt" viewBox="0 0 8 12"><path d="M5 0 L1 6 L4 6 L2 12 L7 5 L4 5 Z" fill="#fff"/></svg>Extra external / internal sockets</li>
    <li><svg class="bolt" viewBox="0 0 8 12"><path d="M5 0 L1 6 L4 6 L2 12 L7 5 L4 5 Z" fill="#fff"/></svg>Garage upgrades</li>
    <li><svg class="bolt" viewBox="0 0 8 12"><path d="M5 0 L1 6 L4 6 L2 12 L7 5 L4 5 Z" fill="#fff"/></svg>LED and low energy lighting installs</li>
  </ul>

  <div class="divider"></div>

  <div class="offer">
    <p class="offer-free">WE OFFER A<br>FREE CONSUMER UNIT<br>AND EARTHING CHECK!</p>
    <p class="offer-hours">24 HOUR SERVICE.</p>
    <p class="offer-text">Prompt Quality Service<br>with Over 15 Years Experience</p>
    <p class="offer-text">All Our Work is Fully Certified<br>and Guaranteed for a Year</p>
    <p class="owner-name">Marcus Pelling</p>
    <p class="owner-role">Owner</p>
  </div>

  <p class="flyer-area">Servicing Devon &amp; Cornwall</p>
  <div class="contact-band">marcus@voltique-wiring.co.uk &nbsp;|&nbsp; www.voltique-wiring.co.uk</div>
  <p class="flyer-phone">07938661207</p>
</section>

<section class="card-front" aria-label="Business card front">
  <div class="card-front-inner">
    <div class="card-brand"><span class="dot"></span><span class="name">VOLTIQUE</span></div>
    <p class="card-area">Servicing Devon &amp; Cornwall</p>
  </div>
</section>

<section class="card-back" aria-label="Business card back">
  <div class="back-band-left"></div>
  <div class="back-band-right"></div>
  <p class="back-name">MARCUS PELLING</p>
  <p class="back-role">OWNER</p>
  <div class="card-brand"><span class="dot"></span><span class="name">VOLTIQUE</span></div>
  <div class="back-divider"></div>
  <ul class="back-contacts">
    <li>07938661207 <svg viewBox="0 0 12 12"><rect width="12" height="12" rx="2" fill="#1b88b3"/><path d="M3.5 2.5 L5 4.5 L4.3 5.4 Q5.3 7 6.6 7.7 L7.5 7 L9.5 8.5 L8.6 9.6 Q5.5 9.6 2.6 5.6 Q2.4 3.4 3.5 2.5 Z" fill="#fff"/></svg></li>
    <li>marcus@voltique-wiring.co.uk <svg viewBox="0 0 12 12"><rect y="2" width="12" height="8" rx="1" fill="#1b88b3"/><path d="M1 3 L6 7 L11 3" stroke="#fff" fill="none"/></svg></li>
    <li>www.voltique-wiring.co.uk <svg viewBox="0 0 12 12"><path d="M2 1 L10 6 L6.5 7 L9 11 L7.5 11.8 L5 7.8 L2 10 Z" fill="#1b88b3"/></svg></li>
  </ul>
  <p class="card-area">Servicing Devon &amp; Cornwall</p>
  <div class="back-footer"></div>
</section>

</body>
</html>
```